kestrova business cards

Hey design gurus!
I'm after a clean, modern, stylish business card for my about to be launched company.
I've uploaded the logos for my company "Kestrova Electrical Solutions"
and also the tarrow alliance logo to whom i am associated.

```html
<!DOCTYPE html>
<html lang="en">
<head>
<meta charset="utf-8">
<title>Kestrova Electrical Solutions – Business Cards</title>
<link href="https://fonts.googleapis.com/css2?family=Poppins:wght@400;500;700&display=swap" rel="stylesheet">
<style>
  :root {
    --stage: #2a2d33;
    --card-black: #050505;
    --card-white: #ffffff;
    --brand-blue: #1b86d6;
    --brand-navy: #1c2a4a;
    --partner-rust: #a5503f;
    --text-light: #ffffff;
    --text-muted: #c9c9c9;
  }
  * { box-sizing: border-box; margin: 0; padding: 0; }
  html, body { width: 1200px; height: 780px; overflow: hidden; }
  body {
    background: var(--stage);
    font-family: "Poppins", sans-serif;
    position: relative;
  }

  /* ---------- Back card (black, portrait) ---------- */
  .card-back {
    position: absolute;
    left: 130px; top: 110px;
    width: 330px; height: 560px;
    background: var(--card-black);
    border-radius: 22px;
    overflow: hidden;
  }
  .back-brand {
    position: absolute;
    left: 34px; top: 46px;
    display: flex; align-items: center; gap: 16px;
  }
  .brand-dot {
    width: 70px; height: 70px;
    border-radius: 50%;
    border: 5px solid var(--brand-blue);
    flex: none;
  }
  .back-brand .brand-name {
    color: var(--brand-blue);
    font-weight: 700;
    font-size: 17px;
    line-height: 1.15;
    text-transform: uppercase;
    letter-spacing: 0.5px;
  }
  .connector {
    position: absolute; left: 0; top: 0;
    width: 330px; height: 560px;
  }
  .contact-item {
    position: absolute;
    display: flex; align-items: flex-start; gap: 12px;
    color: var(--text-light);
  }
  .contact-icon {
    width: 26px; height: 26px;
    border-radius: 50%;
    background: var(--brand-blue);
    flex: none;
    display: flex; align-items: center; justify-content: center;
  }
  .contact-icon.is-light { background: var(--text-light); }
  .contact-text { font-size: 13px; line-height: 19px; }
  .person-name {
    font-size: 24px; font-weight: 500; line-height: 28px;
    text-transform: uppercase;
  }
  .person-name .first { color: var(--brand-blue); }
  .person-role { font-size: 11px; color: var(--text-muted); letter-spacing: 0.5px; }

  /* ---------- Front card (white, landscape) ---------- */
  .card-front {
    position: absolute;
    left: 520px; top: 215px;
    width: 580px; height: 340px;
    background: var(--card-white);
    border-radius: 22px;
  }
  .partner-mark {
    position: absolute;
    right: 60px; top: 48px;
    display: flex; align-items: center; gap: 14px;
  }
  .partner-square {
    width: 46px; height: 46px;
    background: var(--brand-navy);
    border-radius: 6px;
  }
  .partner-name {
    color: var(--partner-rust);
    font-weight: 500;
    font-size: 20px;
    line-height: 1.1;
    text-transform: uppercase;
  }
  .front-brand {
    position: absolute;
    left: 50px; top: 150px;
    color: var(--brand-blue);
    font-weight: 700;
    text-transform: uppercase;
  }
  .front-brand .brand-word { font-size: 62px; line-height: 1; letter-spacing: 2px; }
  .front-brand .brand-sub { font-size: 20px; letter-spacing: 7px; margin-top: 8px; }
</style>
</head>
<body>

  <section class="card-back" aria-label="Business card back">
    <div class="back-brand">
      <span class="brand-dot"></span>
      <div class="brand-name">Kestrova<br>Electrical<br>Solutions</div>
    </div>

    <svg class="connector" viewBox="0 0 330 560" aria-hidden="true">
      <path d="M47 203 V190 Q47 178 59 178 H70" fill="none" stroke="var(--brand-blue)" stroke-width="2"/>
      <path d="M47 203 V470" fill="none" stroke="var(--brand-blue)" stroke-width="2"/>
    </svg>

    <div class="contact-item" style="left:70px; top:165px;">
      <span class="contact-icon">
        <svg width="14" height="14" viewBox="0 0 14 14"><circle cx="7" cy="4.5" r="3" fill="#fff"/><path d="M1.5 13 Q7 6 12.5 13 Z" fill="#fff"/></svg>
      </span>
      <div>
        <div class="person-name"><span class="first">Marlo</span> Quenby</div>
        <div class="person-role">CEO/OWNER</div>
      </div>
    </div>

    <div class="contact-item" style="left:34px; top:260px;">
      <span class="contact-icon is-light">
        <svg width="14" height="14" viewBox="0 0 14 14"><path d="M3 1.5 L5 1.5 L6 4.5 L4.5 5.5 Q5.5 8 8.5 9.5 L9.5 8 L12.5 9 L12.5 11 Q12.5 12.5 11 12.5 Q2 11.5 1.5 3 Q1.5 1.5 3 1.5 Z" fill="var(--brand-blue)"/></svg>
      </span>
      <div class="contact-text">+000 1234 56789<br>+000 1234 56789</div>
    </div>

    <div class="contact-item" style="left:34px; top:320px;">
      <span class="contact-icon">
        <svg width="16" height="16" viewBox="0 0 16 16" fill="none" stroke="#fff" stroke-width="1.3"><circle cx="8" cy="8" r="6.5"/><ellipse cx="8" cy="8" rx="3" ry="6.5"/><path d="M1.5 8 H14.5 M2.5 4.5 H13.5 M2.5 11.5 H13.5"/></svg>
      </span>
      <div class="contact-text">www.yourwesiteurl.com<br>info@yourwebsitename.com</div>
    </div>

    <div class="contact-item" style="left:34px; top:380px;">
      <span class="contact-icon is-light">
        <svg width="12" height="14" viewBox="0 0 12 14"><path d="M6 13.5 Q1 8 1 5.5 A5 5 0 0 1 11 5.5 Q11 8 6 13.5 Z" fill="var(--brand-blue)"/><circle cx="6" cy="5.5" r="2" fill="#fff"/></svg>
      </span>
      <div class="contact-text">Your Address Here<br>Street, City, Country</div>
    </div>
  </section>

  <section class="card-front" aria-label="Business card front">
    <div class="partner-mark">
      <span class="partner-square"></span>
      <div class="partner-name">Tarrow<br>Alliance</div>
    </div>
    <div class="front-brand">
      <div class="brand-word">Kestrova</div>
      <div class="brand-sub">Electrical Solutions</div>
    </div>
  </section>

</body>
</html>
```